Website Design for a New Business Sharing Application

Purpose: Website for a new product – a sharing application called "Gathr.io"

Product concept: Easy sharing of business information. The application has different sections: tasks, calendars, documents, contacts, notes and links. The key feature of the application is that you can drag and drop information from different sections into a "share." A share is a page which lists all the types of information that you drag into it. You can add people to this "share."

Note: The application itself is not part of this project, just the website.

Website details: The site, in addition to being informational, will actually be the first point of entry for visitors into the application itself. Because of that, we would like the website design to reflect the look of the application, to create a smooth and seamless experience for the user moving from the website into the application (tough the website does not need to look *exactly* like the application). Included Product Tour screenshots show you the look of the application.

Website pages to be created: 4 pages
We are flexible in terms of the exact structure and placement of elements. You may change that any way you like. The pages are as follows:

Home page
Product Tour page
Press page
Blog page

Specific description of pages are provided in project files we will upload. We will also upload the logo, home page layout we have in mind, and other supporting files.

NOTE: Please submit first the design of the home page. Based on this design we will ask selected designers to submit designs for the other pages.

Target Market(s)

Business people who want to share work related files with their colleagues

Industry/Entity Type

Business

Requirements
Must have
• All the required features are listed in the description of the website and specific pages that we will upload.

```html
<!DOCTYPE html>
<html lang="en">
<head>
<meta charset="utf-8">
<title>Gathr.io — Gathr.NOW</title>
<link rel="stylesheet" href="https://fonts.googleapis.com/css2?family=Noto+Serif:wght@400;700&family=Shadows+Into+Light+Two&family=Nunito+Sans:wght@700&display=swap">
<style>
:root{
  --bg:#e3e4e5;
  --bg-light:#eceded;
  --band:#d3d4d5;
  --ink:#222;
  --hand:#555;
  --blue:#2a6aa0;
  --navy:#1f4f7c;
  --orange:#d9661e;
  --red:#c0241c;
  --rule:#b9bcbf;
  --paper:#e8e2d2;
  --white:#fff;
}
*{box-sizing:border-box;margin:0;padding:0}
html,body{width:721px;height:1200px;overflow:hidden}
body{
  position:relative;
  background:linear-gradient(160deg,var(--bg-light),var(--bg) 55%,#dfe0e1);
  font-family:"Noto Serif",Georgia,serif;color:var(--ink);
}
.topbar{position:absolute;left:0;top:0;width:721px;height:4px;background:#333}
.abs{position:absolute}
.hand{font-family:"Shadows Into Light Two",cursive;color:var(--hand)}
.brand{left:51px;top:22px;display:flex;align-items:center;gap:10px}
.brand-dot{width:46px;height:46px;border-radius:50%;background:var(--orange)}
.brand-name{font-family:"Nunito Sans",Arial,sans-serif;font-weight:700;font-size:42px;color:var(--navy)}
.note{left:428px;top:8px;width:238px;height:96px;background:var(--paper);transform:rotate(-2deg);box-shadow:0 2px 4px rgba(0,0,0,.15)}
.note p{position:absolute;left:18px;top:22px;font-size:17px;line-height:20px;color:#444}
.note .dot{position:absolute;right:18px;top:16px;width:40px;height:40px;border-radius:50%;background:var(--orange)}
.rule{height:0;border-top:2px dotted var(--rule)}
.vrule{width:0;border-left:2px solid #c9cbcd}
.tag{font-size:17px}
.headline{left:0;width:721px;text-align:center}
.share-now{top:172px;font-size:29px;font-weight:700;color:var(--blue);letter-spacing:1px}
.share-now span{color:var(--orange)}
.boom{top:208px;font-size:19px;font-weight:700}
.types{top:232px;font-size:10px;color:var(--blue);font-weight:700}
.types i{font-style:normal;color:#777;padding:0 3px}
.toolbar{left:241px;top:261px;width:255px;height:39px;border:4px solid #2b2b2b;background:var(--white);display:flex;justify-content:space-around;align-items:center;padding:0 4px}
.toolbar svg{width:18px;height:18px}
.or{left:337px;top:338px;width:40px;height:40px}
.or span{position:absolute;left:10px;top:2px;font-size:26px;color:var(--orange)}
.drop{left:88px;top:427px;width:213px;height:181px;border:4px dashed #b7b9bb;display:flex;align-items:center;justify-content:center}
.mail{left:400px;top:457px;width:239px;height:35px;background:var(--white);box-shadow:0 0 0 3px #f4f4f4;display:flex;align-items:center;justify-content:space-between;padding:0 8px}
.mail span{font-size:13px;color:var(--blue)}
.start{left:533px;top:493px;display:flex;font-size:12px;font-weight:700;color:var(--white)}
.start span{padding:3px 6px}
.start .a{background:var(--navy)}.start .b{background:var(--orange)}
.video{left:380px;top:711px;width:267px;height:142px;background:linear-gradient(#dedfe0,#cfd0d1);border:2px solid #ccc;box-shadow:0 8px 14px rgba(0,0,0,.2);display:flex;align-items:center;justify-content:center;gap:10px}
.video .name{font-family:"Nunito Sans",Arial,sans-serif;font-weight:700;font-size:34px;color:#666}
.play{width:58px;height:58px;border-radius:50%;background:var(--navy);border:3px solid #888;display:flex;align-items:center;justify-content:center}
.what{left:108px;top:779px;width:136px;height:30px;background:var(--navy);border:2px solid #444;color:var(--white);font-size:17px;text-align:center;line-height:26px}
.qmark{left:168px;top:816px;font-size:20px;font-weight:700;color:var(--orange)}
.free{left:222px;top:966px;font-size:13px;color:var(--red);letter-spacing:1px}
.footer-nav{left:68px;top:987px;width:559px;height:30px;background:#e9eaea;border:1px solid #c5c7c9;display:block;text-align:center;line-height:28px;white-space:nowrap;font-size:9.6px;font-weight:700;color:var(--orange)}
.footer-nav i{font-style:normal;color:#888;padding:0 3px}
.footer-nav s{text-decoration-color:var(--red)}
.band{left:0;top:1113px;width:721px;height:87px;background:var(--band)}
.social{position:absolute;width:74px;height:74px;border-radius:50%;background:#f1f1f1;border:3px solid #c7c8c9;display:flex;align-items:center;justify-content:center;font-family:"Nunito Sans",Arial,sans-serif;font-weight:700;font-size:11px;color:var(--navy);top:1120px}
</style>
</head>
<body>
<div class="topbar"></div>

<header>
  <div class="abs brand"><div class="brand-dot"></div><span class="brand-name">Gathr.io</span></div>
  <a class="abs note hand"><p>Click here to<br>Access your shares</p><span class="dot"></span></a>
</header>

<div class="abs rule" style="left:87px;top:123px;width:560px"></div>

<section class="hero">
  <p class="abs hand tag" style="left:100px;top:132px">Certified fastest sharing in the market</p>
  <p class="abs hand tag" style="left:496px;top:132px">It's social!</p>
  <svg class="abs" style="left:228px;top:154px" width="60" height="46" viewBox="0 0 60 46"><path d="M55 40 C30 44 14 36 12 8 M4 16 L12 6 L20 16" fill="none" stroke="#777" stroke-width="2"/></svg>
  <svg class="abs" style="left:466px;top:162px" width="68" height="40" viewBox="0 0 68 40"><path d="M4 34 C30 36 50 26 60 8 M48 8 L61 6 L60 18" fill="none" stroke="#777" stroke-width="2"/></svg>
  <h1 class="abs headline share-now">Gathr.<span>NOW</span></h1>
  <p class="abs headline boom">Drag information, add people, BOOM!</p>
  <p class="abs headline types">files<i>|</i>pictures<i>|</i>tasks<i>|</i>to-dos<i>|</i>calendars<i>|</i>notes<i>|</i>links</p>
  <nav class="abs toolbar" aria-label="Sections">
    <svg viewBox="0 0 18 18"><path d="M1 9 L9 2 L17 9 H14 V16 H4 V9 Z" fill="#222"/></svg>
    <svg viewBox="0 0 18 18"><circle cx="9" cy="6" r="4" fill="#222"/><path d="M2 17 C2 11 16 11 16 17Z" fill="#222"/></svg>
    <svg viewBox="0 0 18 18"><rect x="2" y="2" width="14" height="14" fill="none" stroke="#222" stroke-width="2"/><path d="M5 9 L8 12 L14 5" fill="none" stroke="#222" stroke-width="2"/></svg>
    <svg viewBox="0 0 18 18"><rect x="1" y="4" width="16" height="12" fill="#222"/><circle cx="6" cy="9" r="2" fill="#fff"/><rect x="10" y="8" width="5" height="2" fill="#fff"/></svg>
    <svg viewBox="0 0 18 18"><path d="M7 11 L11 7 M6 8 L3 11 A3 3 0 0 0 7 15 L10 12 M8 6 L11 3 A3 3 0 0 1 15 7 L12 10" fill="none" stroke="#222" stroke-width="2"/></svg>
    <svg viewBox="0 0 18 18"><rect x="2" y="3" width="14" height="13" fill="none" stroke="#222" stroke-width="2"/><path d="M2 7 H16 M6 10 H8 M10 10 H12 M6 13 H8 M10 13 H12" stroke="#222" stroke-width="2"/></svg>
    <svg viewBox="0 0 18 18"><rect x="2" y="2" width="13" height="14" fill="none" stroke="#222" stroke-width="2"/><path d="M5 6 H12 M5 9 H12 M5 12 H9" stroke="#222" stroke-width="1.5"/></svg>
    <svg viewBox="0 0 18 18"><circle cx="9" cy="9" r="7" fill="none" stroke="#222" stroke-width="2"/><path d="M6 9 L8 11 L12 6" fill="none" stroke="#222" stroke-width="2"/></svg>
    <svg viewBox="0 0 18 18"><path d="M4 1 H11 L15 5 V17 H4 Z" fill="#222"/></svg>
  </nav>
</section>

<div class="abs rule" style="left:87px;top:315px;width:560px"></div>

<section class="start-area">
  <div class="abs or">
    <svg width="40" height="40" viewBox="0 0 40 40"><path d="M6 14 A15 15 0 0 1 34 12 M34 26 A15 15 0 0 1 6 28" fill="none" stroke="#aaa" stroke-width="3"/></svg>
    <span class="hand">or</span>
  </div>
  <p class="abs hand" style="left:87px;top:360px;font-size:20px">drag files here to share</p>
  <svg class="abs" style="left:276px;top:386px" width="40" height="56" viewBox="0 0 40 56"><path d="M4 4 C34 6 36 30 20 48 M12 42 L20 50 L26 40" fill="none" stroke="#666" stroke-width="2"/></svg>
  <div class="abs drop" aria-label="Drop files here">
    <svg width="76" height="76" viewBox="0 0 76 76"><path d="M30 0 H46 V30 H76 V46 H46 V76 H30 V46 H0 V30 H30 Z" fill="#bdbec0"/></svg>
  </div>
  <div class="abs vrule" style="left:356px;top:387px;height:240px"></div>
  <p class="abs hand" style="left:409px;top:360px;font-size:20px">enter your business mail</p>
  <svg class="abs" style="left:500px;top:392px" width="40" height="50" viewBox="0 0 40 50"><path d="M6 4 C12 20 22 30 32 42 M22 42 L33 44 L32 32" fill="none" stroke="#666" stroke-width="2"/></svg>
  <label class="abs mail"><span>Enter business mail</span>
    <svg width="24" height="16" viewBox="0 0 24 16"><rect x="1" y="1" width="22" height="14" fill="none" stroke="#bbb"/><path d="M1 1 L12 9 L23 1" fill="none" stroke="#bbb"/></svg>
  </label>
  <svg class="abs" style="left:470px;top:496px" width="54" height="18" viewBox="0 0 54 18"><path d="M2 9 H50 M42 3 L51 9 L42 15" fill="none" stroke="#777" stroke-width="2"/></svg>
  <div class="abs start"><span class="a">Start</span><span class="b">Sharing</span></div>
</section>

<div class="abs rule" style="left:75px;top:645px;width:572px"></div>

<section class="tour">
  <div class="abs vrule" style="left:361px;top:667px;height:240px"></div>
  <p class="abs hand" style="left:389px;top:662px;font-size:20px">video tour</p>
  <svg class="abs" style="left:470px;top:660px" width="50" height="34" viewBox="0 0 50 34"><path d="M2 10 C20 2 36 6 42 26 M34 20 L42 28 L48 18" fill="none" stroke="#666" stroke-width="2"/></svg>
  <div class="abs video" aria-label="Product video">
    <span class="name">Gathr.io</span>
    <span class="play"><svg width="24" height="26" viewBox="0 0 24 26"><path d="M3 1 L23 13 L3 25 Z" fill="#fff"/></svg></span>
  </div>
  <p class="abs hand" style="left:107px;top:748px;font-size:20px">what is it</p>
  <a class="abs what">what is it</a>
  <span class="abs qmark">?</span>
</section>

<div class="abs rule" style="left:75px;top:920px;width:572px"></div>

<footer>
  <p class="abs hand free">Free for unlimited users</p>
  <nav class="abs footer-nav">Home<i>|</i>About us<i>|</i>Product Tour<i>|</i><s>Pricing</s><i>|</i>Terms of use<i>|</i>Jobs<i>|</i>Sign up<i>|</i>Blog<i>|</i>Press<i>|</i>Contact us</nav>
  <p class="abs hand" style="left:291px;top:1074px;font-size:20px">social sharing!</p>
  <svg class="abs" style="left:410px;top:1072px" width="74" height="46" viewBox="0 0 74 46"><path d="M2 12 C30 2 58 8 64 36 M56 30 L64 40 L70 28" fill="none" stroke="#555" stroke-width="2"/></svg>
  <div class="abs band"></div>
  <a class="social" style="left:80px">Chirply</a>
  <a class="social" style="left:190px">Snapfold</a>
  <a class="social" style="left:312px">Kinbook</a>
  <a class="social" style="left:435px">Newsline</a>
  <a class="social" style="left:551px">Clipcast</a>
</footer>
</body>
</html>
```